Awesome law firm seeks great artwork for sign to be installed at local roller skating rink!!

We're a dynamic, law firm that does its work with a difference - we actually care about our clients and our fees are usually lower than most other firms.

We are installing a sign that's 78cm (height) x 158cm (width) to be printed on 3mm Aluminum Composite Panel and installed at a local roller skating rink in Kalamunda, Perth, Western Australia.

Graphics need to be provided in vector .eps (Encapsulated Post Script), .ai (Adobe Illustrator) or PDF format.

We have uploaded a copy of our Logo, which should feature on the sign (we usually have it on the top right of our stationery, but are happy to see other suggestions), together with our practice areas - Family Law, Wills and Estates, Building and Construction, Corporate and Commercial, Local Government, General legal (personal or business).

We don't have a 'slogan' for our firm, but for the roller skating rink sign, we're thinking of something like 'We roll with you", or something similar. Surprise us :)

Sign should also indicate that our team are local to "the Hills", which is how this area (the Kalamunda and surrounding areas of Perth) is known.

Main colors of the sign can include blue, white, black and red (more blue, white and black preferred).

The final design should communicate trust and expertise in law, but have a fun edge (the sign's at a roller skating rink after all and will be seen on every lap as it's in the rink).

The sign must include our website address www.venkarilegal.com (note this is still under construction in case you google us :)), our phone number 0431 508 279 and our main email address, which is admin@venkarilegal.com

Beyond this, we're happy to see any cool ideas for the design of our sign.

Target Market(s)

Local families and business owners at local roller skating rink

Industry/Entity Type

Legal services

Font styles to use
Serif
Other font styles liked:
• Designer to choose

Colors
0054AA
0677BA
7BADD7
CADEEF
E8F1F8
EB3D1F
EC4F4E
F09395
F8D3D4
FCEDEE

Requirements
Must have
• Logo, contact details, design as per description and can have the words "Get your skates on!"
Nice to have
• Awesome, striking, appealing design - easy to read as you're zooming past on your skates!
Should not have
• Any offensive, explicit, corny or suggestive words and preferably avoid cliché rhyming catch phrases, albeit we do want something fun that has a skating vibe

```html
<!DOCTYPE html>
<html lang="en">
<head>
<meta charset="utf-8">
<title>Venkari Legal – Rink Sign</title>
<link href="https://fonts.googleapis.com/css2?family=Tinos:ital,wght@0,400;0,700;1,400&family=Montserrat:wght@600;700&display=swap" rel="stylesheet">
<style>
  :root{
    --page:#e2e2e2;
    --navy-deep:#070f26;
    --navy:#142a5c;
    --navy-glow:#4a6aa8;
    --rule:#2f5fb5;
    --white:#ffffff;
    --ink:#1b2550;
    --accent:#EB3D1F;
    --sky:#7BADD7;
    --floor-top:#5d6b82;
    --floor-bottom:#b7bfca;
  }
  *{margin:0;padding:0;box-sizing:border-box}
  html,body{width:748px;height:1200px;overflow:hidden;background:var(--page)}
  .sign{
    position:absolute;left:24px;top:427px;width:700px;height:345px;
    background:var(--white);
    box-shadow:0 14px 26px rgba(0,0,0,.35);
    overflow:hidden;
  }
  .sign__panel{
    position:absolute;left:0;top:0;width:700px;height:297px;
    background:
      radial-gradient(ellipse 230px 200px at 300px 190px, var(--navy-glow) 0%, rgba(74,106,168,0) 100%),
      linear-gradient(100deg, var(--navy) 0%, #1d3670 40%, var(--navy-deep) 100%);
  }
  .sign__floor{
    position:absolute;left:0;top:262px;width:700px;height:35px;
    background:linear-gradient(180deg,var(--floor-top),var(--floor-bottom));
  }
  .brand{
    position:absolute;left:38px;top:28px;
    font-family:"Tinos",serif;font-weight:400;color:var(--white);line-height:1;
  }
  .brand__line1{display:block;font-size:27px;letter-spacing:.5px}
  .brand__line2{display:block;font-size:38px;letter-spacing:2px;margin-top:4px}
  .photo{position:absolute}
  .photo--gavel{
    left:0;top:113px;width:170px;height:184px;
    background:linear-gradient(160deg,#8a5a2e 0%,#5a3a1e 35%,#d8cfb8 60%,#3d4a3e 100%);
    border-radius:2px 6px 0 0;
  }
  .photo--justice{
    left:238px;top:42px;width:106px;height:252px;
    background:linear-gradient(180deg,#b08a55 0%,#3e3a2c 40%,#2a3a36 70%,#111 100%);
    border-radius:40px 40px 6px 6px;
  }
  .practice{position:absolute;left:372px;top:52px;width:310px;height:170px}
  .practice__item{
    position:absolute;width:145px;height:38px;
    display:flex;align-items:center;gap:10px;
    font-family:"Montserrat",sans-serif;font-weight:600;font-size:12.5px;line-height:1.2;color:var(--white);
    white-space:nowrap;
  }
  .practice__item--ruled::after{
    content:"";position:absolute;left:0;right:0;bottom:-8px;height:1px;background:var(--rule);
  }
  .practice__icon{width:29px;height:29px;flex:0 0 29px;background:var(--white);display:flex;align-items:center;justify-content:center}
  .practice__icon svg{width:21px;height:21px;stroke:var(--ink);fill:none;stroke-width:1.4}
  .tagline{
    position:absolute;left:372px;top:214px;width:310px;
    font-family:"Tinos",serif;color:var(--white);line-height:1.15;
  }
  .tagline__slogan{display:block;font-size:21px;font-weight:700}
  .tagline__slogan em{font-style:italic;color:var(--sky)}
  .tagline__local{display:block;margin-top:3px;font-family:"Montserrat",sans-serif;font-weight:700;font-size:10.5px;letter-spacing:1.6px;text-transform:uppercase;color:var(--white)}
  .tagline__dot{display:inline-block;width:6px;height:6px;border-radius:50%;background:var(--accent);margin-right:7px;vertical-align:1px}
  .contact{
    position:absolute;left:0;top:297px;width:700px;height:48px;
    display:flex;align-items:center;justify-content:center;gap:9px;
    font-family:"Tinos",serif;font-size:16.5px;color:#333;white-space:nowrap;
  }
  .contact__icon{width:26px;height:26px;background:var(--ink);display:flex;align-items:center;justify-content:center}
  .contact__icon svg{width:16px;height:16px;stroke:var(--white);fill:none;stroke-width:1.5}
  .contact__domain{font-weight:700;color:var(--ink)}
  .contact__phone{font-weight:700;color:#3a3f4e;font-size:18px}
  .contact__sep{width:1px;height:20px;background:var(--ink);margin:0 4px}
</style>
</head>
<body>
<main class="sign">
  <div class="sign__panel"></div>
  <div class="sign__floor"></div>

  <div class="brand">
    <span class="brand__line1">VENKARI</span>
    <span class="brand__line2">LEGAL</span>
  </div>

  <div class="photo photo--gavel" role="img" aria-label="Photo of a wooden judge's gavel resting on a stack of law books"></div>
  <div class="photo photo--justice" role="img" aria-label="Photo of a bronze Lady Justice statue holding scales and a sword"></div>

  <section class="practice">
    <div class="practice__item practice__item--ruled" style="left:0;top:0">
      <span class="practice__icon"><svg viewBox="0 0 24 24"><circle cx="8" cy="8" r="3"/><circle cx="16" cy="9" r="2.5"/><path d="M3 20v-3a5 5 0 0 1 10 0v3M12 20v-2a4 4 0 0 1 8 0v2"/></svg></span>
      <span>Family<br>Law</span>
    </div>
    <div class="practice__item practice__item--ruled" style="left:165px;top:0">
      <span class="practice__icon"><svg viewBox="0 0 24 24"><path d="M12 3v17M6 20h12M4 7h16M4 7l-2 6h4zM20 7l-2 6h4z"/></svg></span>
      <span>Local<br>Government</span>
    </div>
    <div class="practice__item practice__item--ruled" style="left:0;top:56px">
      <span class="practice__icon"><svg viewBox="0 0 24 24"><path d="M5 3h11v18H5zM8 7h5M8 10h5M8 13h3M16 6h3v4h-3"/></svg></span>
      <span>Wills and<br>Estates</span>
    </div>
    <div class="practice__item practice__item--ruled" style="left:165px;top:56px">
      <span class="practice__icon"><svg viewBox="0 0 24 24"><path d="M5 21V5h14v16M3 21h18M8 8h2M14 8h2M8 12h2M14 12h2M8 16h2M14 16h2"/></svg></span>
      <span>Corporate and<br>Commercial</span>
    </div>
    <div class="practice__item" style="left:0;top:112px">
      <span class="practice__icon"><svg viewBox="0 0 24 24"><path d="M3 9l9-5 9 5zM5 9v9M9 9v9M15 9v9M19 9v9M3 20h18"/></svg></span>
      <span>General<br>legal</span>
    </div>
    <div class="practice__item" style="left:165px;top:112px">
      <span class="practice__icon"><svg viewBox="0 0 24 24"><path d="M6 21V4M3 5h16M6 4l4 1M17 5v4M12 21v-8h8v8M14 16h1M17 16h1M3 21h18"/></svg></span>
      <span>Building and<br>Construction</span>
    </div>
  </section>

  <div class="tagline">
    <span class="tagline__slogan">Get your skates on — <em>we've got your back.</em></span>
    <span class="tagline__local"><span class="tagline__dot"></span>Your local lawyers in the Hills</span>
  </div>

  <footer class="contact">
    <span class="contact__icon"><svg viewBox="0 0 24 24"><rect x="3" y="6" width="18" height="12"/><path d="M3 6l9 7 9-7"/></svg></span>
    <span>admin@<span class="contact__domain">venkarilegal</span>.com</span>
    <span class="contact__sep"></span>
    <span class="contact__icon"><svg viewBox="0 0 24 24"><circle cx="12" cy="12" r="9"/><path d="M3 12h18M12 3c3 3 3 15 0 18M12 3c-3 3-3 15 0 18"/></svg></span>
    <span>www.<span class="contact__domain">venkarilegal</span>.com</span>
    <span class="contact__sep"></span>
    <span class="contact__icon"><svg viewBox="0 0 24 24"><path d="M6 3l3 4-2 2a11 11 0 0 0 8 8l2-2 4 3-2 3C10 21 3 14 3 5z"/></svg></span>
    <span class="contact__phone">0431 508 279</span>
  </footer>
</main>
</body>
</html>
```